Company Website

We need an interactive website designed that for new company. Our company is in the Automotive fleet maintenance business. We have wide ranging customers in many industries e.g Aviation industry, construction industry, transportation etc.
We would like the website to have login accounts where customers can register, login and access their service history. Also we would like to have an appointment system where customers could schedule appointments, once appointments are made that time would no longer be available to be selected as it would be booked etc.

The website should also be updatable and provide areas for showcasing
Our services
Products/parts (possibly store front)
Customer feedback
Appointments
Our customers (where our customers can advertise or be showcased)
About us
Contacts
gallery

We would like designs that have a modern, corporate feel, One that is user friendly.
prefer a design that does not look like a template.

Target Market(s)

Medium to large companies, small business owners and the general motoring public.

Industry/Entity Type

Construction

Requirements
Must have
• Customer login set up so a database of customer vehicle maintenance history as well as the ability to schedule repairs via their account. They could also check the status of a repair.
Nice to have
• Photo gallery to show case current projects.
Our customers page where we can show case our clients they could also post their events on there, promotions etc.

The theme Should be something that's reflective of our core business; fleet maintenance. It would be nice to capture some sort of background in there that depicts some of that for example mixer trucks, tractors,loaders excavators forklifts cars trucks. That's what we deal with. It's up to the designer to capture the Essence of this as much as possible. Impress me.
Should not have
• Would prefer a custom website not a template.

```html
<!DOCTYPE html>
<html lang="en">
<head>
<meta charset="utf-8">
<title>Keystone Fleet &amp; Auto Maintenance</title>
<link href="https://fonts.googleapis.com/css2?family=Arimo:wght@400;700&family=Archivo+Black&display=swap" rel="stylesheet">
<style>
:root{
  --red:#b3171d;
  --red-dark:#8f1015;
  --ink:#222;
  --text:#555;
  --muted:#999;
  --topbar:#222;
  --btn-dark:#4a4a4a;
  --panel:#ececec;
  --line:#c9c9c9;
  --white:#fff;
}
*{box-sizing:border-box;margin:0;padding:0}
html,body{width:1050px;height:1200px;overflow:hidden;background:var(--white)}
body{position:relative;font-family:"Arimo",Arial,sans-serif;color:var(--text)}
.abs{position:absolute}

.topbar{left:0;top:0;width:1050px;height:26px;background:var(--topbar)}
.topbar .social{left:656px;top:4px;display:flex;gap:6px}
.dot{width:19px;height:19px;border-radius:50%;background:#777;display:block}
.topbar .link{top:0;height:26px;line-height:26px;color:#fff;font-size:12px;display:flex;align-items:center;gap:5px;white-space:nowrap}
.topbar .sep{left:829px;top:0;width:1px;height:26px;background:#444}

.hero-bg{left:0;top:26px;width:1050px;height:430px;
  background:linear-gradient(180deg,#d9d9d9 0%,#e8e8e8 55%,rgba(255,255,255,1) 100%);}
.hero-bg::after{content:"";position:absolute;inset:0;
  background:linear-gradient(90deg,rgba(200,190,150,.35) 0%,rgba(255,255,255,0) 20%,rgba(255,255,255,0) 80%,rgba(200,120,120,.3) 100%)}

.brand{left:150px;top:44px;width:200px;color:var(--red);font-weight:700;white-space:nowrap}
.brand .name{font-size:27px;letter-spacing:1px;line-height:30px;display:flex;align-items:center;gap:6px}
.brand .name i{display:block;width:14px;height:14px;background:var(--red);border-radius:50%}
.brand .sub{font-size:10px;line-height:14px;padding-left:14px}

.phone{right:150px;top:62px;font-size:20px;color:#444;display:flex;align-items:center;gap:6px;white-space:nowrap}

.nav{left:150px;top:122px;width:751px;height:27px;background:var(--white);display:flex;align-items:center;box-shadow:0 2px 3px rgba(0,0,0,.12)}
.nav .home{flex:0 0 30px;width:30px;height:27px;background:var(--red);display:flex;align-items:center;justify-content:center}
.nav ul{list-style:none;display:flex;flex-wrap:nowrap;padding-left:11px;font-size:10px;color:var(--red);white-space:nowrap}
.nav li{flex-shrink:0}
.nav li+li::before{content:"|";padding:0 5px;color:var(--red)}

.hero-panel{left:150px;top:149px;width:751px;height:300px;background:rgba(255,255,255,.88)}
.hero-copy{left:162px;top:194px;width:380px}
.hero-copy .k1{font-size:19px;color:var(--ink);line-height:22px}
.hero-copy .k2{font-size:44px;font-weight:700;color:var(--red);line-height:40px}
.hero-copy .k3{font-size:33px;font-weight:700;color:var(--ink);line-height:34px}
.hero-copy p{margin-top:8px;font-size:11.5px;line-height:13.6px;color:#444}
.pager{left:162px;top:372px;display:flex;gap:4px}
.pager span{width:17px;height:3px;background:#444}
.pager span.on{background:var(--red)}
.hero-photo{left:542px;top:197px;width:352px;height:171px;border-radius:6px;
  background:linear-gradient(160deg,#f4f4f4,#d4d4d4)}
.arrow{width:32px;height:32px;border-radius:50%;background:rgba(255,255,255,.85);border:1px solid #ccc;display:flex;align-items:center;justify-content:center}

.btn{top:410px;height:34px;width:216px;color:#fff;font-size:15px;display:flex;align-items:center;justify-content:center;gap:8px;box-shadow:0 2px 3px rgba(0,0,0,.25);white-space:nowrap}
.btn.red{background:var(--red);justify-content:flex-start;padding-left:8px}
.btn.dark{background:linear-gradient(#5a5a5a,#3e3e3e)}

.claim{left:0;top:482px;width:1050px;text-align:center;font-family:"Archivo Black",Arial,sans-serif;font-size:23px;line-height:28px;color:var(--red)}
.claim b{color:var(--ink);font-weight:400}

.projects{left:150px;top:560px;width:752px;height:195px;background:var(--panel)}
.projects .band{position:absolute;left:0;top:0;width:752px;height:150px;background:var(--red)}
.projects h2{position:absolute;left:8px;top:12px;font-size:17px;font-weight:400;color:#fff}
.projects .rule{position:absolute;left:8px;right:8px;top:37px;border-top:1px dashed rgba(255,255,255,.35)}
.card{position:absolute;top:46px;width:180px}
.card .ph{width:180px;height:113px;background:linear-gradient(180deg,#f2f2f2,#bdbdbd);box-shadow:0 2px 3px rgba(0,0,0,.2)}
.card .t{text-align:center;font-size:13px;color:#666;margin-top:6px}
.card .s{text-align:center;font-size:8px;color:#aaa}

.welcome{left:157px;top:789px;width:513px}
.welcome h2{font-size:16px;font-weight:400;color:var(--ink);padding-bottom:4px;border-bottom:1px dashed var(--line);white-space:nowrap}
.welcome h2 span{color:var(--red);font-weight:700;font-size:15.5px}
.wtext{font-size:10.3px;line-height:12.5px;color:#666}
.w1{left:159px;top:830px;width:362px}
.w2{left:159px;top:921px;width:510px}
.welcome-photo{left:532px;top:831px;width:144px;height:70px;border-radius:4px;background:linear-gradient(160deg,#f4f4f4,#cfcfcf)}

.news{left:684px;top:787px;width:217px}
.news h2{font-size:16px;font-weight:400;color:var(--ink);padding-bottom:4px;border-bottom:1px dashed var(--line)}
.item{position:absolute;left:684px;display:flex;gap:7px;white-space:nowrap}
.item .th{width:47px;height:32px;background:linear-gradient(#f0f0f0,#c6c6c6);border:1px solid #ddd}
.item .d{font-size:11.5px;color:var(--red);line-height:14px}
.item .x{font-size:8px;color:#555}

.footer{left:150px;top:1002px;width:750px;height:149px;background:var(--panel)}
.col{position:absolute;top:1024px;font-size:8px;line-height:11.3px;color:#999;white-space:nowrap}
.col h3{font-size:11.5px;font-weight:400;color:#666;margin-bottom:6px}
.col .icons{display:flex;gap:3px}
.col .icons .dot{width:20px;height:20px;background:var(--red)}
.foot-brand{left:0;top:1117px;width:1050px;text-align:center;color:var(--red);font-weight:700}
.foot-brand .name{font-size:20px;line-height:22px}
.foot-brand .sub{font-size:8px}
.copy{left:0;top:1180px;width:1050px;text-align:center;font-size:7.5px;color:#777}
</style>
</head>
<body>

<div class="abs hero-bg" role="img" aria-label="Faded background photo of fleet vehicles: excavators, loaders and trucks"></div>

<header class="abs topbar">
  <div class="abs social"><span class="dot"></span><span class="dot"></span><span class="dot" style="background:#4a6fb5"></span><span class="dot"></span></div>
  <div class="abs link" style="left:764px">Register
    <svg width="10" height="12" viewBox="0 0 10 12"><rect x="1" y="2" width="8" height="9.5" fill="none" stroke="#fff" stroke-width="1.2"/><rect x="3" y="0.5" width="4" height="2.5" fill="#fff"/></svg></div>
  <div class="abs sep"></div>
  <div class="abs link" style="left:842px">Login
    <svg width="13" height="12" viewBox="0 0 13 12"><path d="M6.5 0v6M4 4l2.5 2.5L9 4" stroke="#fff" stroke-width="1.6" fill="none"/><rect x="1" y="7" width="11" height="4" rx="1" fill="#fff"/></svg></div>
</header>

<div class="abs brand">
  <div class="name"><i></i>KEYSTONE</div>
  <div class="sub">FLEET &amp; AUTO MAINTENANCE</div>
</div>

<div class="abs phone">
  <svg width="18" height="18" viewBox="0 0 18 18"><rect x="1" y="3" width="16" height="13" rx="2" fill="var(--red)"/><rect x="4" y="1" width="10" height="4" rx="1" fill="var(--red)"/><g fill="#fff"><rect x="5" y="8" width="2" height="2"/><rect x="8" y="8" width="2" height="2"/><rect x="11" y="8" width="2" height="2"/><rect x="5" y="11" width="2" height="2"/><rect x="8" y="11" width="2" height="2"/><rect x="11" y="11" width="2" height="2"/></g></svg>
  + 10 20 30 40 50
</div>

<div class="abs hero-panel"></div>

<nav class="abs nav">
  <div class="home"><svg width="14" height="13" viewBox="0 0 14 13"><path d="M7 1L1 6.5h2V12h3V8.5h2V12h3V6.5h2z" fill="none" stroke="#fff" stroke-width="1.4"/></svg></div>
  <ul>
    <li>OUR SERVICES</li><li>PRODUCTS/PARTS</li><li>CUSTOMER FEEDBACK</li><li>APPOINTMENTS</li><li>OUR CUSTOMERS</li><li>ABOUT US</li><li>CONTACTS</li><li>GALLERY</li>
  </ul>
</nav>

<section class="abs hero-copy">
  <div class="k1">AUTOMOTIVE</div>
  <div class="k2">FLEET</div>
  <div class="k3">MAINTENANCE</div>
  <p>At Keystone we sell a service, one stop location where our customers can get their mechanical needs fulfilled. We do offer products in the form of mechanical parts and a few promotional gear. Our services extend to much more than repairs in shop. We can handle jobs on site with our mobile service vehicles, refueling services, highly skilled technicians.</p>
</section>
<div class="abs pager"><span></span><span class="on"></span><span></span><span></span></div>
<div class="abs hero-photo" role="img" aria-label="White mobile service truck with crane"></div>

<div class="abs arrow" style="left:107px;top:260px"><svg width="14" height="10" viewBox="0 0 14 10"><path d="M5 1L1 5l4 4M1 5h12" stroke="var(--red)" stroke-width="1.5" fill="none"/></svg></div>
<div class="abs arrow" style="left:912px;top:260px"><svg width="14" height="10" viewBox="0 0 14 10"><path d="M9 1l4 4-4 4M13 5H1" stroke="#555" stroke-width="1.5" fill="none"/></svg></div>

<div class="abs btn red" style="left:150px">MAKE AN APPOINTMENT
  <svg width="20" height="18" viewBox="0 0 20 18"><rect x="3" y="2" width="13" height="14" rx="1" fill="none" stroke="#fff" stroke-width="1.3" transform="rotate(-15 10 9)"/><path d="M6 7h7M6 10h7M6 13h5" stroke="#fff" stroke-width="1.1" transform="rotate(-15 10 9)"/></svg></div>
<div class="abs btn dark" style="left:415px">REGISTER NOW
  <svg width="13" height="17" viewBox="0 0 13 17"><rect x="1" y="2.5" width="11" height="14" fill="none" stroke="#fff" stroke-width="1.3"/><rect x="4" y="0.5" width="5" height="3" fill="#fff"/><path d="M3.5 7h6M3.5 10h6M3.5 13h6" stroke="#fff"/></svg></div>
<div class="abs btn dark" style="left:685px">OUR SERVICES
  <svg width="18" height="18" viewBox="0 0 18 18"><circle cx="9" cy="9" r="5.5" fill="none" stroke="#fff" stroke-width="3" stroke-dasharray="2.4 1.9"/><circle cx="9" cy="9" r="4" fill="#fff"/><circle cx="9" cy="9" r="1.8" fill="#444"/></svg></div>

<h1 class="abs claim">WE ARE CERTIFIED TECHNICIANS AND HAVE<br>OVER <b>40YEARS</b> COMBINED EXPERIENCE</h1>

<section class="abs projects">
  <div class="band"></div>
  <h2>Current projects</h2>
  <div class="rule"></div>
  <div class="card" style="left:9px"><div class="ph" role="img" aria-label="Yellow concrete mixer truck"></div><div class="t">Lorem ipsum</div><div class="s">See more...</div></div>
  <div class="card" style="left:194px"><div class="ph" role="img" aria-label="Mixer drum assembly"></div><div class="t">Lorem ipsum dolor</div><div class="s">See more...</div></div>
  <div class="card" style="left:378px"><div class="ph" role="img" aria-label="Red pickup truck"></div><div class="t">Lorem ipsum</div><div class="s">See more...</div></div>
  <div class="card" style="left:563px"><div class="ph" role="img" aria-label="Tractor cutaway"></div><div class="t">Lorem ipsum dolor</div><div class="s">See more...</div></div>
</section>

<section class="abs welcome">
  <h2>Welcome to <span>KEYSTONE FLEET AND AUTO MAINTENANCE</span></h2>
</section>
<p class="abs wtext w1">Lorem ipsum dolor sit amet, consectetuer adipiscing elit, sed diam nonummy nibh euismod tincidunt ut laoreet dolore magna aliquam erat volutpat. Ut wisi enim ad minim veniam, quis nostrud exerci tation ullamcorper suscipit lobortis nisl ut aliquip ex ea commodo consequat. Duis autem vel eum iriure dolor in hendrerit in vulputate velit esse molestie consequat, vel illum dolore eu feugiat nulla facilisis at vero eros et accumsan et iusto odio dignissim qui blandit praesent luptatum zzril delenit augue duis dolore te feugait nulla facilisi.</p>
<div class="abs welcome-photo" role="img" aria-label="Mobile service truck"></div>
<p class="abs wtext w2">Lorem ipsum dolor sit amet, consectetuer adipiscing elit, sed diam nonummy nibh euismod tincidunt ut laoreet dolore magna aliquam erat volutpat. Ut wisi enim ad minim veniam, quis nostrud exerci tation ullamcorper suscipit lobortis nisl ut aliquip ex ea commodo consequat.</p>

<section class="abs news"><h2>Services News</h2></section>
<div class="item" style="top:816px"><div class="th" role="img" aria-label="Mixer drum"></div><div><div class="d">November 2013</div><div class="x">Lorem ipsum dolor sit ampet</div></div></div>
<div class="item" style="top:855px"><div class="th" role="img" aria-label="Tractor"></div><div><div class="d">August 2013</div><div class="x">Lorem ipsum dolor sit ampet</div></div></div>
<div class="item" style="top:893px"><div class="th" role="img" aria-label="Service truck"></div><div><div class="d">November 2013</div><div class="x">Lorem ipsum dolor sit ampet</div></div></div>
<div class="item" style="top:929px"><div class="th" role="img" aria-label="Mixer truck"></div><div><div class="d">August 2013</div><div class="x">Lorem ipsum dolor sit ampet</div></div></div>

<footer class="abs footer"></footer>
<div class="col" style="left:166px"><h3>INFORMATION</h3>Lorem ipsum dolor sit ampet<br>Lorem ipsum dolor<br>Lorem ipsum dolor sit<br>Lorem ipsum</div>
<div class="col" style="left:355px"><h3>SERVICES</h3>Fleet maintenance<br>Equipment inspections<br>Engine repair<br>Complete refurbishing<br>Preventative maintenance<br>Zero-time rebuilds</div>
<div class="col" style="left:545px"><h3>CONTACT</h3>Keystone fleet and auto<br>maintenance.<br>City 123, CA, US.<br>tlf. 10 20 30 40 50<br>email. info@keystonefleet.example</div>
<div class="col" style="left:734px"><h3>SOCIAL MEDIA</h3><div class="icons"><span class="dot" style="background:#3b5998"></span><span class="dot"></span><span class="dot" style="background:#4a6fb5"></span><span class="dot" style="background:#2aa3d8"></span></div></div>

<div class="abs foot-brand"><div class="name">KEYSTONE</div><div class="sub">FLEET &amp; AUTO MAINTENANCE</div></div>
<div class="abs copy">COPYRIGHT © 2014 KEYSTONE FLEET AND AUTO MAINTENANCE. ALL RIGHTS RESERVED.</div>

</body>
</html>
```